Short presentation of new electrical engineering company

i just founded a new company and would like to send a short presentation to selected potential new customers. So they know that there is a new company and what we do. I am looking for a short presentation since i believe it is too long, nobody will read it. i need it in english and german, but i can provide both texts. i thought, it should be a short version of my existing homepage www.velunor.ch on paper Prefered format: A5 or A4 landscape folded. Reason is that i can send it easily with mail. The design should be technical, electrical engineering, provide the important information as contact information, some referenc work, and the range of service. i have no other design requirements. it should just look great ;-)

Target Market(s)

Production Companies which could be electrical engineer freelancers

Industry/Entity Type

Engineering

Font styles to use
Sans Serif

Requirements
Must have
• German and English Version Either A5 double side or A4 folded double side. Reason is that you have to send it by mail and do not want to fold it in the middle of the design
Nice to have
• Some different layouts as my drafts would be nice i am curious what else could be done

```html
<!DOCTYPE html>
<html lang="de">
<head>
<meta charset="utf-8">
<title>Velunor GmbH – Electrical Automation Engineering</title>
<link rel="stylesheet" href="https://fonts.googleapis.com/css2?family=Source+Sans+3:wght@400;600;700&display=swap">
<style>
  :root {
    --navy: #1f2660;
    --head-a: #2b2f78;
    --head-b: #5a5aa8;
    --sky: #1e9ad6;
    --sky-light: #2aa6e0;
    --panel: #f2f2f4;
    --ink: #1c1c1c;
    --white: #ffffff;
  }
  * { box-sizing: border-box; margin: 0; padding: 0; }
  html, body { width: 950px; height: 1200px; overflow: hidden; background: #ffffff; }
  body { font-family: "Source Sans 3", Arial, sans-serif; color: var(--ink); }
  .flyer { position: relative; width: 950px; height: 1200px; background: var(--white); }

  .brand { position: absolute; top: 38px; left: 0; width: 950px; text-align: center; color: var(--navy); }
  .brand-name { font-size: 48px; font-weight: 700; letter-spacing: 2px; line-height: 1; }
  .brand-tag { font-size: 13px; font-weight: 700; letter-spacing: 2px; margin-top: 6px; }

  .photos { position: absolute; top: 154px; left: 0; width: 950px; height: 189px; display: flex; }
  .photo { height: 100%; }
  .photo-terminals { width: 381px; background: linear-gradient(160deg, #d9dde2 0%, #8c96a3 45%, #3f8f74 70%, #c8cdd2 100%); }
  .photo-board { width: 310px; background: linear-gradient(170deg, #e4e2df 0%, #9aa08a 45%, #4b4a3e 75%, #9b9891 100%); }
  .photo-plc { width: 259px; background: linear-gradient(150deg, #c9c8c2 0%, #5d5f62 40%, #3c3d40 65%, #ddd8c8 100%); }

  .intro { position: absolute; top: 343px; left: 0; width: 950px; height: 168px; background: var(--sky); color: var(--white); }
  .intro-title { position: absolute; left: 49px; top: 14px; width: 300px; font-size: 28px; font-weight: 700; line-height: 35px; }
  .intro-rule { position: absolute; left: 352px; top: 20px; width: 1px; height: 128px; background: rgba(255,255,255,.75); }
  .intro-text { position: absolute; left: 385px; top: 21px; width: 520px; font-size: 14px; line-height: 18.5px; text-align: justify; }
  .intro-text p + p { margin-top: 11px; }

  .service { position: absolute; background: var(--panel); border: 1px solid var(--navy); }
  .service::after { content: ""; position: absolute; left: 12%; right: 12%; bottom: -9px; height: 8px; border-radius: 50%; background: radial-gradient(ellipse at center, rgba(0,0,0,.35), rgba(0,0,0,0) 70%); }
  .service-head { height: 34px; background: linear-gradient(90deg, var(--head-a), var(--head-b)); color: var(--white); font-size: 20px; font-weight: 600; letter-spacing: .3px; display: flex; align-items: center; padding-left: 10px; gap: 12px; overflow: hidden; }
  .service-head svg { flex: none; }
  .service-list { list-style: none; padding: 8px 4px 0 32px; font-size: 13.5px; line-height: 16.5px; white-space: nowrap; }
  .service-list li + li { margin-top: 5px; }
  .service-list.loose li + li { margin-top: 11px; }

  .row-1 { top: 566px; height: 265px; }
  .row-2 { top: 859px; height: 199px; }
  .col-1 { left: 47px; width: 260px; }
  .col-2 { left: 349px; width: 260px; }
  .col-3 { left: 641px; width: 261px; }

  .footer { position: absolute; top: 1098px; left: 0; width: 950px; height: 80px; background: var(--navy); color: var(--white); font-size: 13.5px; line-height: 18px; }
  .footer-strip { position: absolute; top: 1178px; left: 0; width: 950px; height: 22px; background: var(--sky-light); }
  .footer-col { position: absolute; top: 10px; }
  .footer-contact { left: 46px; }
  .footer-contact .label { margin-bottom: 7px; }
  .footer-address { left: 375px; top: 14px; }
  .footer-address .web { font-weight: 700; margin-top: 10px; font-size: 14.5px; }
  .footer-terms { left: 675px; }
  .footer-terms .label { margin-bottom: 6px; }
  .footer-rule { position: absolute; top: 12px; width: 1px; height: 58px; background: rgba(255,255,255,.6); }
</style>
</head>
<body>
<main class="flyer">
  <header class="brand">
    <div class="brand-name">Velunor</div>
    <div class="brand-tag">Electrical Automation Engineering</div>
  </header>

  <section class="photos">
    <div class="photo photo-terminals" role="img" aria-label="Foto: Reihenklemmen in einem Schaltschrank"></div>
    <div class="photo photo-board" role="img" aria-label="Foto: bestückte Leiterplatte mit Bauteilen"></div>
    <div class="photo photo-plc" role="img" aria-label="Foto: Steuerungsmodul im Schaltschrank"></div>
  </section>

  <section class="intro">
    <h1 class="intro-title">Gemeinsam Herausforderungen Meistern Und Ziele Erreichen</h1>
    <div class="intro-rule"></div>
    <div class="intro-text">
      <p>Die Firma Velunor Electrical Automation Engineering unterstützt Sie in Ihren Anliegen betreffend allen Bereichen der Elektro-technik und der Automation.</p>
      <p>Wir sind Spezialisten in dem entwerfen von Steuerungen, programmieren der SPS, erstellen von Visualisierungen, auslegen von Antriebsleistungen und der Inbetriebnahme aller Komponenten vor Ort. Dies jeweils unter Berücksichtigung aller gängigen Nor-men und Standards.</p>
    </div>
  </section>

  <section class="service row-1 col-1">
    <h2 class="service-head">ENGINEERING
      <svg width="30" height="30" viewBox="0 0 30 30" fill="none" stroke="#fff" stroke-width="1.3"><circle cx="15" cy="15" r="5"/><path d="M15 3l2 4 4-1 1 4 4 2-2 3 2 3-4 2-1 4-4-1-2 4-2-4-4 1-1-4-4-2 2-3-2-3 4-2 1-4 4 1z"/></svg>
    </h2>
    <ul class="service-list">
      <li>Beratungen, Konzepte und<br>Machbar-keitsstudien zu<br>Automatisierungsanla-gen</li>
      <li>Service und Support</li>
      <li>Entwicklung von Produkten</li>
      <li>Innovationen im Bereich<br>Elektrotech-nik</li>
      <li>Verbesserungen bestehender Abläufe<br>oder Produkten</li>
      <li>Gesamt-Projektleitung</li>
      <li>Offerten und Preisschätzungen</li>
    </ul>
  </section>

  <section class="service row-1 col-2">
    <h2 class="service-head">PROGRAMMIERUNG
      <svg width="40" height="24" viewBox="0 0 40 24" fill="none" stroke="#fff" stroke-width="1"><path d="M2 2v20M38 2v20M2 8h9M15 8h10M29 8h9M11 4v8M15 4v8M25 4v8M29 4v8M2 16h9M15 16h23M11 13v6M15 13v6"/></svg>
    </h2>
    <ul class="service-list">
      <li>Norvik ControlDesk 7</li>
      <li>Norvik Unity Studio</li>
      <li>Kalder Electric FlowBench</li>
      <li>Brightwell CoreLogic 500</li>
      <li>Erstellen von Visualisierungen auf<br>ver-schiedenen Plattformen</li>
      <li>Programmieren von Desktopanwen-<br>dungen mit C#</li>
      <li>KOP, FUP, AWL oder SCL</li>
    </ul>
  </section>

  <section class="service row-1 col-3">
    <h2 class="service-head">ANTRIEBSTECHNIK</h2>
    <ul class="service-list loose">
      <li>Auslegung von Antriebsleistungen</li>
      <li>Evaluation der geeigneten<br>Antriebsart</li>
      <li>Parametrieren von<br>Frequenzumrich-tern<br>verschiedener Hersteller</li>
      <li>Verbessern des Wirkungsgrades</li>
    </ul>
  </section>

  <section class="service row-2 col-1">
    <h2 class="service-head">STEUERUNGEN
      <svg width="52" height="22" viewBox="0 0 52 22" fill="none" stroke="#fff" stroke-width="1"><path d="M0 11h18M34 11h18M18 4h16v14H18zM20 16l12-10M40 7v8M46 7v8"/></svg>
    </h2>
    <ul class="service-list">
      <li>Planen von Automatisierungslösungen</li>
      <li>Erstellen von Konzepten und Schemas</li>
      <li>Modernisieren von bestehenden<br>Steu-erungen</li>
      <li>Hersteller-Unabhängig</li>
    </ul>
  </section>

  <section class="service row-2 col-2">
    <h2 class="service-head">INBETRIEBNAHMEN</h2>
    <ul class="service-list">
      <li>Inbetriebnahmen von Steuerungen,<br>Anlagen und Antrieben Weltweit</li>
      <li>Lösungsfindung und beheben von<br>auftretenden Problemen vor Ort</li>
      <li>Durchführen der geforderten<br>Ab-schlusstests nach erfolgreicher<br>Inbe-triebnahme</li>
    </ul>
  </section>

  <section class="service row-2 col-3">
    <h2 class="service-head">RISIKOANALYSEN</h2>
    <ul class="service-list">
      <li>Durchführen von<br>Gefährdungsabschät-zungen</li>
      <li>Minimieren der Gefahren gemäss<br>EN 13849</li>
      <li>Erstellen der nötigen<br>Nachweisdoku-menten</li>
      <li>Software Reviews von bestehen-<br>dem Code</li>
    </ul>
  </section>

  <footer class="footer">
    <div class="footer-col footer-contact">
      <div class="label">KONTAKT</div>
      <div>MARCO KELLER: +41 79 000 12 34</div>
      <div>M.KELLER@VELUNOR.CH</div>
    </div>
    <div class="footer-rule" style="left:344px"></div>
    <div class="footer-col footer-address">
      <div>Velunor Gmbh,&nbsp; Marco Keller</div>
      <div>Mattenweg 7, 6430 Schwyz</div>
      <div class="web">www.velunor.ch</div>
    </div>
    <div class="footer-rule" style="left:627px"></div>
    <div class="footer-col footer-terms">
      <div class="label">KONDITIONEN BIS 01/08/2018</div>
      <div>INLAND CH: 112 CHF exkl./Std.</div>
      <div>AUSLAND: ZUS. 100FR Spesen/Tag.</div>
    </div>
  </footer>
  <div class="footer-strip"></div>
</main>
</body>
</html>
```